MD Business Card

I want to create a simple business card.
I am a consultant. I design and develop furniture, lighting and accessories for hospitality and retail brands.
I want the card to be simple and clean. Not too much of a logo - but it needs the basic information shown on the attached file.
Also - I have shown some fonts that I like on the attached file.
The card can be square or rectangle. It should be double sided.
I prefer 1-2 colors (not too colorful - but using color an an accent) Even if using color on the edges as an accent.

My snapquilt link shows some other graphics styles that I like. I like clean and simple.
http://www.snapquilt.com/marendowsett/business-cards/

Reason: I needed a few more days to see some of the options evolve.

Hospitality

```html
<!DOCTYPE html>
<html lang="en">
<head>
<meta charset="utf-8">
<title>Maren Dowsett — Business Card</title>
<link rel="stylesheet" href="https://fonts.googleapis.com/css2?family=Advent+Pro:wght@500&display=swap">
<style>
  :root {
    --backdrop: #e4e1dc;
    --card: #ffffff;
    --ink: #141414;
    --accent: #6e8c72;
  }
  * { margin: 0; padding: 0; box-sizing: border-box; }
  html, body {
    width: 1060px;
    height: 1200px;
    overflow: hidden;
    background: var(--backdrop);
  }
  .card {
    position: absolute;
    left: 42px;
    width: 978px;
    height: 558px;
    background: var(--card);
    color: var(--ink);
    font-family: "Advent Pro", sans-serif;
    font-weight: 500;
  }
  .card--front { top: 25px; }
  .card--back { top: 604px; }

  .brand {
    position: absolute;
    top: 232px;
    left: 0;
    width: 100%;
    text-align: center;
  }
  .brand__name {
    display: inline-flex;
    align-items: center;
    gap: 16px;
    font-weight: 500;
    font-size: 48px;
    line-height: 1;
    letter-spacing: 5px;
    text-transform: uppercase;
  }
  .brand__mark {
    width: 14px;
    height: 14px;
    background: var(--accent);
  }
  .brand__tagline {
    margin-top: 70px;
    font-size: 36px;
    letter-spacing: 4.5px;
    line-height: 1;
  }

  .contact {
    position: absolute;
    left: 78px;
    top: 118px;
    font-style: normal;
    font-size: 32px;
    letter-spacing: 3.5px;
    line-height: 38px;
  }
  .contact__phone { letter-spacing: 5px; }
  .services {
    position: absolute;
    left: 252px;
    top: 462px;
    font-size: 32px;
    letter-spacing: 3.5px;
    word-spacing: 24px;
    line-height: 1;
  }
</style>
</head>
<body>
  <section class="card card--front">
    <div class="brand">
      <h1 class="brand__name"><span class="brand__mark"></span>Maren Dowsett</h1>
      <p class="brand__tagline">hospitality &amp; home</p>
    </div>
  </section>

  <section class="card card--back">
    <address class="contact">
      maren@marendowsett.com<br>
      <span class="contact__phone">917.555.0148</span>
    </address>
    <p class="services">ff&amp;e furniture lighting textiles</p>
  </section>
</body>
</html>
```